Ruvo Decor

There is a sample provided with the arabic text of the business card. please copy paste the same text and the same Logo (The two triangles) Just try to incorproate the Brown background attached (you are free to change the colors) Id like the colors to be mainly shades of black and red.

```html
<!DOCTYPE html>
<html lang="ar">
<head>
<meta charset="utf-8">
<title>Ruvo Decor – Business Card</title>
<link rel="stylesheet" href="https://fonts.googleapis.com/css2?family=Aref+Ruqaa:wght@400;700&family=Tajawal:wght@400;700&family=Lalezar&family=Roboto:wght@500&display=swap">
<style>
  :root {
    --red: #c8202a;
    --red-deep: #8c0d12;
    --black: #0b0b0b;
    --white: #ffffff;
    --page: #ffffff;
  }
  html, body {
    margin: 0;
    padding: 0;
    width: 1200px;
    height: 1200px;
    overflow: hidden;
    background: var(--page);
  }
  .canvas { position: relative; width: 1200px; height: 1200px; }
  .card {
    position: absolute;
    left: 191px;
    width: 839px;
    height: 475px;
    border-radius: 34px 0 34px 0;
    overflow: hidden;
    background: var(--black);
  }
  .card--front { top: 110px; }
  .card--back  { top: 636px; }
  .card svg { display: block; width: 839px; height: 475px; }
  .rtl { direction: rtl; unicode-bidi: embed; text-anchor: start; }
  .title-name  { font-family: "Aref Ruqaa", serif; font-size: 40px; fill: var(--white); }
  .title-role  { font-family: "Aref Ruqaa", serif; font-size: 38px; fill: var(--red); }
  .credential  { font-family: "Tajawal", sans-serif; font-size: 29px; fill: var(--white); }
  .contact     { font-family: "Roboto", sans-serif; font-weight: 500; fill: var(--white); }
  .contact--mail  { font-size: 20px; }
  .contact--phone { font-size: 27px; }
  .brand { font-family: "Tajawal", sans-serif; font-weight: 700; font-size: 44px; fill: var(--white); }
  .service { font-family: "Lalezar", sans-serif; font-size: 32px; fill: var(--white); }
</style>
</head>
<body>
<main class="canvas">

  <section class="card card--front">
    <svg viewBox="0 0 839 475" xmlns="http://www.w3.org/2000/svg">
      <defs>
        <radialGradient id="texture-front" cx="0.35" cy="0.45" r="0.75">
          <stop offset="0" stop-color="#e8323a"/>
          <stop offset="0.5" stop-color="#b0141b"/>
          <stop offset="1" stop-color="#2a0304"/>
        </radialGradient>
      </defs>
      <rect class="texture" role="img" aria-label="Red abstract grid texture background" width="839" height="475" fill="url(#texture-front)"/>
      <polygon class="info-panel" points="466,0 839,0 839,475 472,475 300,234" fill="var(--black)"/>
      <polygon class="contact-band" points="439,372 839,372 839,446 486,446" fill="var(--red)"/>

      <text class="title-name rtl" x="784" y="100">المهندس/ سامي فؤاد الراشد</text>
      <text class="title-role rtl" x="698" y="166">أستاذ جامعي</text>

      <text class="credential rtl" x="786" y="218" textLength="306" lengthAdjust="spacingAndGlyphs">ماجستير هندسة ديكور</text>
      <text class="credential rtl" x="786" y="254" textLength="306" lengthAdjust="spacingAndGlyphs">دبلوم عالي فن تشكيلي</text>
      <text class="credential rtl" x="786" y="290" textLength="306" lengthAdjust="spacingAndGlyphs">أكاديمية الريم للفنون</text>
      <text class="credential rtl" x="786" y="326" textLength="306" lengthAdjust="spacingAndGlyphs">استشارات هندسية - فنية</text>

      <text class="contact contact--mail" x="472" y="398" textLength="282" lengthAdjust="spacingAndGlyphs">sami.rashed@ruvodecor.com</text>
      <g class="icon-mail" transform="translate(763,384)" fill="none" stroke="var(--white)" stroke-width="1.8">
        <rect x="0" y="0" width="24" height="16"/>
        <polyline points="0,0 12,9 24,0"/>
      </g>
      <text class="contact contact--phone" x="476" y="433" textLength="280" lengthAdjust="spacingAndGlyphs">39104526 / 66521847</text>
      <path class="icon-phone" transform="translate(764,414)" fill="var(--white)"
            d="M4 1c2-1 4 0 5 2l1 3c0 1-1 2-2 3 0 2 2 5 4 6 1-1 2-2 3-1l3 2c1 1 1 3 0 4-2 2-4 2-7 0-5-3-9-8-10-13 0-3 1-5 3-6z"/>

      <g class="brand-mark">
        <rect x="82" y="230" width="26" height="26" fill="var(--white)"/>
        <text class="brand" x="118" y="258">Ruvo Decor</text>
      </g>
    </svg>
  </section>

  <section class="card card--back">
    <svg viewBox="0 0 839 475" xmlns="http://www.w3.org/2000/svg">
      <defs>
        <radialGradient id="texture-back" cx="0.18" cy="0.3" r="0.8">
          <stop offset="0" stop-color="#f07a40"/>
          <stop offset="0.15" stop-color="#d8252c"/>
          <stop offset="0.55" stop-color="#9a1016"/>
          <stop offset="1" stop-color="#220203"/>
        </radialGradient>
      </defs>
      <rect class="texture" role="img" aria-label="Red abstract grid texture with light flare" width="839" height="475" fill="url(#texture-back)"/>
      <polygon class="dark-band" points="380,120 839,0 839,475 500,475" fill="var(--black)"/>
      <polygon class="service-panel" points="263,120 839,12 839,396 440,475" fill="var(--red)"/>
      <polygon class="corner-accent" points="744,475 839,412 839,475" fill="var(--red)"/>

      <g class="brand-mark">
        <rect x="36" y="356" width="24" height="24" fill="var(--white)"/>
        <text class="brand" x="68" y="382">Ruvo Decor</text>
      </g>

      <g class="service-list">
        <text class="service rtl" x="782" y="118">ديكور عام</text>
        <text class="service rtl" x="782" y="162">ديكورات/ منازل/ فلل/ مكاتب/ حدائق</text>
        <text class="service rtl" x="782" y="204">ديكورات محلات تجارية</text>
        <text class="service rtl" x="782" y="245">ديكورات مسارح أعراس/ مهرجانات</text>
        <text class="service rtl" x="782" y="287">تخصص بديكورات تراثية بحرينية قديمة</text>
        <text class="service rtl" x="782" y="329">ديكورات فنادق</text>
      </g>
      <g class="bullets" fill="var(--black)">
        <polygon points="796,98 812,98 804,114"/>
        <polygon points="796,142 812,142 804,158"/>
        <polygon points="796,184 812,184 804,200"/>
        <polygon points="796,225 812,225 804,241"/>
        <polygon points="796,267 812,267 804,283"/>
        <polygon points="796,309 812,309 804,325"/>
      </g>
    </svg>
  </section>

</main>
</body>
</html>
```